Simple, Elegant, Clean Homepage Design For Hirevane.com - for job seekers.

Hello, we're going to start this site by posting a project for ONE page of it - the homepage. I've attached a simple wireframe I created and we'll be using logo #1 in the attached PDF.

Anyway, all the wireframe shows is where the elements should be. You'll put in placeholder image(s) where needed. (i.e. The BrightDesk banner.)

We are looking for a simple, clean site - very minimalistic but also one that grabs the eye.

Simple, clean menu across the top...the little links at the bottom...

And in the middle show us some headline styles, subhead styles, body copy font style, and bullets we can use.

As you can see there is also a search tool for employers in the upper right, so we'd like to see your vision of that as well.

Thanks!

Tom

P.S. You can just put in some garbled example text to illustrate fonts and other elements listed in the description.

P.P.S. I just added a new PDF to this project showing some updated tag lines we like with the "hirevane.com/your-name-here" thing we like. See if this can be integrated into your existing designs - or new designs.

Target Market(s)

Job Seekers

Number of Pages Required

1 page

Font styles to use
Sans Serif

Colors
ffffff
0456a4
000000
c5c5c5

Requirements
Must have
• Must be a simple, clean, optimized HTML/CSS design. We are looking for a minimalistic approach, so that we can easily highlight certain features/text/icons with color.
Nice to have
• White background, elegant and "soft" outlines for sections, easy to read font, headline fonts/colors that grab, tasteful bullets.
Should not have
• Complex design
• hard to read fonts
• busy/loud design
• not too serious, not too casual

```html
<!DOCTYPE html>
<html lang="en">
<head>
<meta charset="utf-8">
<title>Hirevane — Home</title>
<link href="https://fonts.googleapis.com/css2?family=Raleway:wght@600;700;800&family=Open+Sans:wght@400;600&display=swap" rel="stylesheet">
<style>
  :root {
    --blue: #0456a4;
    --ink: #222222;
    --muted: #6b6b6b;
    --line: #c5c5c5;
    --page: #f7f7f7;
    --white: #ffffff;
    --footer: #333333;
    --black: #1a1a1a;
  }
  * { box-sizing: border-box; margin: 0; padding: 0; }
  html, body { width: 1200px; height: 1116px; overflow: hidden; }
  body {
    position: relative;
    background: var(--page);
    font-family: "Open Sans", Arial, sans-serif;
    color: var(--ink);
  }

  /* Header */
  .brand {
    position: absolute; left: 96px; top: 32px;
    display: flex; align-items: center; gap: 10px;
  }
  .brand-dot { width: 34px; height: 34px; border-radius: 50%; background: var(--blue); }
  .brand-name {
    font-family: "Raleway", Arial, sans-serif; font-weight: 700;
    font-size: 36px; color: var(--blue); letter-spacing: -0.5px;
  }
  .main-nav a {
    position: absolute; top: 47px;
    font-family: "Raleway", Arial, sans-serif; font-weight: 700;
    font-size: 15.5px; color: var(--ink); text-decoration: none;
  }
  .candidate-search {
    position: absolute; left: 825px; top: 39px; width: 276px; height: 36px; display: flex;
  }
  .candidate-search input {
    flex: 1; height: 36px; border: 1px solid var(--line); border-right: 0;
    background: var(--white); padding: 0 16px;
    font-family: "Open Sans", Arial, sans-serif; font-size: 14px; color: var(--muted);
  }
  .candidate-search input::placeholder { color: #777; }
  .candidate-search button {
    width: 41px; height: 36px; border: 0; background: var(--blue);
    display: flex; align-items: center; justify-content: center;
  }

  /* Hero */
  .hero {
    position: absolute; left: 99px; top: 115px; width: 681px; height: 344px;
    background: linear-gradient(115deg, #b7a08a 0%, #8a5a32 28%, #4a3426 55%, #2f2b2a 78%, #5a6570 100%);
    overflow: hidden;
  }
  .hero::after {
    content: ""; position: absolute; inset: 0;
    background: radial-gradient(ellipse at 70% 20%, rgba(230,150,70,.35), transparent 60%);
  }
  .hero-title {
    position: absolute; left: 0; right: 0; top: 90px; z-index: 1;
    text-align: center; color: var(--white);
    font-family: "Raleway", Arial, sans-serif; font-weight: 800;
    font-size: 45px; line-height: 51px; letter-spacing: -0.5px;
    text-shadow: 0 2px 6px rgba(0,0,0,.35);
  }
  .play-button {
    position: absolute; left: 313px; top: 209px; width: 54px; height: 54px; z-index: 1;
    border-radius: 50%; background: rgba(20,20,20,.85);
    display: flex; align-items: center; justify-content: center;
  }

  /* Promo card */
  .promo {
    position: absolute; left: 803px; top: 115px; width: 298px; height: 344px;
    background: var(--blue); overflow: hidden; color: var(--white);
  }
  .promo-photo {
    position: absolute; left: 0; top: 0; width: 298px; height: 280px;
    background: linear-gradient(160deg, #4a4f55 0%, #9aa2aa 40%, #d9dde0 65%, #6d7278 100%);
  }
  .promo-wave { position: absolute; left: 0; top: 220px; }
  .promo-title {
    position: absolute; left: 16px; top: 268px;
    font-family: "Raleway", Arial, sans-serif; font-weight: 700; font-size: 22px;
  }
  .promo-sub { position: absolute; left: 16px; top: 303px; font-size: 14px; }
  .register-button {
    position: absolute; left: 179px; top: 296px; width: 106px; height: 36px;
    border-radius: 18px; background: var(--black); color: var(--white);
    display: flex; align-items: center; justify-content: center; gap: 7px;
    font-family: "Open Sans", Arial, sans-serif; font-weight: 600; font-size: 13px; letter-spacing: .3px;
  }

  /* Welcome */
  .welcome-title {
    position: absolute; left: 0; right: 0; top: 534px; text-align: center;
    font-family: "Raleway", Arial, sans-serif; font-weight: 800; font-size: 31px; color: var(--ink);
  }
  .welcome-copy {
    position: absolute; left: 250px; width: 700px; top: 591px; text-align: center;
    font-size: 14.5px; line-height: 24px; color: var(--muted);
  }

  /* Features */
  .feature {
    position: absolute; top: 690px; width: 314px; height: 264px;
    background: var(--white); box-shadow: 0 0 4px rgba(0,0,0,.08); text-align: center;
  }
  .feature-icon { position: absolute; left: 0; right: 0; top: 26px; height: 82px; display: flex; justify-content: center; }
  .feature-title {
    position: absolute; left: 0; right: 0; top: 139px;
    font-family: "Raleway", Arial, sans-serif; font-weight: 700; font-size: 20.5px; color: var(--ink);
  }
  .feature-text {
    position: absolute; left: 20px; right: 20px; top: 181px;
    font-size: 14px; line-height: 25px; color: var(--muted);
  }

  /* Footer */
  .site-footer {
    position: absolute; left: 0; top: 1041px; width: 1200px; height: 75px;
    background: var(--footer); color: var(--white); font-size: 13px;
  }
  .copyright { position: absolute; left: 97px; top: 27px; }
  .footer-links { position: absolute; right: 99px; top: 26px; display: flex; gap: 15px; }
  .footer-links a { color: var(--white); text-decoration: none; }
  .footer-links span { color: var(--white); }
</style>
</head>
<body>

<header class="site-header">
  <div class="brand">
    <span class="brand-dot"></span>
    <span class="brand-name">hirevane</span>
  </div>
  <nav class="main-nav">
    <a href="#" style="left:388px">ABOUT</a>
    <a href="#" style="left:471px">SUPPORT</a>
    <a href="#" style="left:572px">SIGN IN</a>
    <a href="#" style="left:663px">FREE TRAINING</a>
  </nav>
  <form class="candidate-search">
    <input type="text" placeholder="Search Candidates">
    <button type="button" aria-label="Search">
      <svg width="17" height="17" viewBox="0 0 20 20"><circle cx="8.5" cy="8.5" r="6" fill="none" stroke="#fff" stroke-width="2.8"/><line x1="13" y1="13" x2="18" y2="18" stroke="#fff" stroke-width="3" stroke-linecap="round"/></svg>
    </button>
  </form>
</header>

<section class="hero" role="img" aria-label="Photo of colleagues talking around a laptop in a warm office">
  <h1 class="hero-title">Because you’re<br>more than just a resume</h1>
  <span class="play-button">
    <svg width="22" height="24" viewBox="0 0 22 24"><path d="M4 2 L20 12 L4 22 Z" fill="#fff"/></svg>
  </span>
</section>

<aside class="promo">
  <div class="promo-photo" role="img" aria-label="Photo of a laptop showing an online course page beside a coffee cup"></div>
  <svg class="promo-wave" width="298" height="70" viewBox="0 0 298 70">
    <path d="M0 30 C60 10 110 30 160 45 C210 58 260 40 298 15 L298 70 L0 70 Z" fill="#c9ccd0"/>
    <path d="M0 38 C60 18 110 38 160 52 C210 64 262 48 298 24 L298 70 L0 70 Z" fill="#0456a4"/>
  </svg>
  <div class="promo-title">BrightDesk</div>
  <div class="promo-sub">Finibus Bonorut Malo</div>
  <span class="register-button">
    <svg width="12" height="12" viewBox="0 0 12 12"><path d="M1 11 L1.6 8.4 L8.4 1.6 L10.4 3.6 L3.6 10.4 Z" fill="#fff"/></svg>
    REGISTER
  </span>
</aside>

<section class="welcome">
  <h2 class="welcome-title">WELCOME TO HIREVANE</h2>
  <p class="welcome-copy">Nam libero tempore, cum soluta nobis est eligendi optio cumque nihil impedit quo minus id quod maxime placeat facere possimus, omnis voluptas assumenda est, omnis dolor repellendus.</p>
</section>

<section class="features">
  <article class="feature" style="left:99px">
    <div class="feature-icon">
      <svg width="56" height="82" viewBox="0 0 56 82">
        <path d="M28 6 C14 6 6 16 6 27 C6 38 16 44 17 56 L39 56 C40 44 50 38 50 27 C50 16 42 6 28 6 Z" fill="none" stroke="#0456a4" stroke-width="7"/>
        <path d="M22 20 C27 18 33 20 34 26" fill="none" stroke="#0456a4" stroke-width="4" stroke-linecap="round"/>
        <rect x="16" y="58" width="24" height="7" rx="3.5" fill="#0456a4"/>
        <rect x="16" y="66" width="24" height="7" rx="3.5" fill="#0456a4"/>
        <rect x="20" y="73" width="16" height="7" rx="3.5" fill="#0456a4"/>
      </svg>
    </div>
    <h3 class="feature-title" style="top:143px">Business Skills</h3>
    <p class="feature-text" style="top:185px">Nam libero tempore, cum soluta no bis est eligendi optio cumque nihil impe</p>
  </article>

  <article class="feature" style="left:443px">
    <div class="feature-icon">
      <svg width="82" height="82" viewBox="0 0 82 82">
        <path d="M0 45 L82 0 L70 76 L48 62 L40 80 L34 56 Z" fill="#0456a4"/>
        <path d="M34 56 L82 0 L48 62 Z" fill="#ffffff" opacity=".25"/>
      </svg>
    </div>
    <h3 class="feature-title">Faster and Easier</h3>
    <p class="feature-text">Nam libero tempore, cum soluta no bis est eligendi optio cumque nihil impe</p>
  </article>

  <article class="feature" style="left:788px">
    <div class="feature-icon" style="top:33px">
      <svg width="70" height="70" viewBox="0 0 70 70">
        <circle cx="35" cy="35" r="35" fill="#0456a4"/>
        <ellipse cx="35" cy="35" rx="14" ry="33" fill="none" stroke="#fff" stroke-width="2.5"/>
        <line x1="2" y1="35" x2="68" y2="35" stroke="#fff" stroke-width="2.5"/>
        <path d="M7 20 H63 M7 50 H63" stroke="#fff" stroke-width="2.5"/>
      </svg>
    </div>
    <h3 class="feature-title">Anytime, Anywhere</h3>
    <p class="feature-text">Nam libero tempore, cum soluta no bis est eligendi optio cumque nihil impe</p>
  </article>
</section>

<footer class="site-footer">
  <p class="copyright">Copyrights © 2017, hirevane.com.&nbsp; All rights reserved.</p>
  <nav class="footer-links">
    <a href="#">Contact</a><span>|</span>
    <a href="#">Terms</a><span>|</span>
    <a href="#">Disclaimer</a><span>|</span>
    <a href="#">Privacy</a><span>|</span>
    <a href="#">Sign In</a><span>|</span>
    <a href="#">Directory</a>
  </nav>
</footer>

</body>
</html>
```